Website Redesign for Brightfen Forgeworks

We are looking for a high-end Minimalist Design That will give potential customers the feel that they are purchasing a hand-crafted reproduction of an actual historical medieval sword. The tone or feel should like a luxury sword manufacturer.
Perhaps having a darker background with logo/text that pops more with a white glow.

Target Market(s)

Historical "efficinato" - educated history buffs interested in high end swords & armors, with a available capital for such a hobby.

Number of Pages Required

3 page

Font styles to use
Serif

Colors
1b1b1b
000000
e6e6e6
c9c9c9

Requirements
Must have
• -cart page
• -home page
• -1 product page
Nice to have
• -large images
• - Garamon or Centaur font
• - Our logo is in Trojan Pro
Should not have
• -no excessive use of colors
• -no medieval / gothic fonts

```html
<!DOCTYPE html>
<html lang="en">
<head>
<meta charset="UTF-8">
<title>Brightfen Forgeworks — Medieval Swords</title>
<link rel="stylesheet" href="https://fonts.googleapis.com/css2?family=Oswald:wght@400&family=PT+Serif:wght@400;700&family=Montserrat:wght@400&display=swap">
<style>
  :root {
    --stage: #f1f1f1;
    --ink-black: #000000;
    --ink-dark: #1b1b1b;
    --ink-light: #e6e6e6;
    --ink-muted: #c9c9c9;
    --white: #ffffff;
  }
  * { margin: 0; padding: 0; box-sizing: border-box; }
  html, body {
    width: 1200px;
    height: 1200px;
    overflow: hidden;
    background: var(--stage);
  }
  .site {
    position: absolute;
    left: 0;
    top: 225px;
    width: 1200px;
    height: 750px;
    background: var(--ink-dark);
    overflow: hidden;
    color: var(--white);
  }
  .hero-image {
    position: absolute;
    inset: 0;
    background:
      linear-gradient(150deg, rgba(60,60,60,0.35) 0%, rgba(0,0,0,0) 45%),
      linear-gradient(30deg, #141414 0%, #262626 40%, #1e1e1e 65%, #0e0e0e 100%);
  }
  .nav {
    position: absolute;
    top: 94px;
    display: flex;
    gap: 9px;
    font-family: "Oswald", sans-serif;
    font-size: 13px;
    letter-spacing: 0.06em;
    text-transform: uppercase;
    color: var(--ink-light);
    list-style: none;
  }
  .nav li + li::before {
    content: "|";
    margin-right: 9px;
    color: var(--ink-muted);
  }
  .nav-left { left: 163px; }
  .nav-right { right: 208px; }
  .brand {
    position: absolute;
    left: 0;
    right: 0;
    top: 36px;
    text-align: center;
    font-family: "PT Serif", serif;
    font-weight: 700;
    color: var(--white);
    text-shadow: 0 0 14px rgba(255,255,255,0.25);
  }
  .brand-mark {
    display: block;
    width: 46px;
    height: 46px;
    margin: 0 auto 10px;
    border-radius: 50%;
    background: var(--white);
  }
  .brand-name {
    font-size: 32px;
    line-height: 1.05;
  }
  .headline {
    position: absolute;
    left: 0;
    right: 0;
    top: 259px;
    text-align: center;
    font-family: "PT Serif", serif;
    font-weight: 700;
    font-size: 58px;
    line-height: 74px;
    color: var(--white);
  }
  .intro {
    position: absolute;
    left: 0;
    right: 0;
    top: 435px;
    text-align: center;
    font-family: "PT Serif", serif;
    font-size: 18.5px;
    line-height: 32px;
    color: var(--ink-muted);
  }
  .cta {
    position: absolute;
    left: 504px;
    top: 551px;
    width: 191px;
    height: 39px;
    border: 1.5px solid var(--ink-light);
    border-radius: 10px;
    font-family: "Montserrat", sans-serif;
    font-size: 14px;
    letter-spacing: 0.2em;
    color: var(--ink-light);
    display: flex;
    align-items: center;
    justify-content: center;
    text-decoration: none;
  }
  .slider-dots {
    position: absolute;
    left: 560px;
    top: 689px;
  }
</style>
</head>
<body>
  <main class="site">
    <div class="hero-image" role="img" aria-label="Close-up photograph of two crossed pattern-welded medieval swords in dark monochrome"></div>

    <ul class="nav nav-left">
      <li>Home</li>
      <li>Medieval Swords</li>
      <li>Armors</li>
      <li>Daggers</li>
    </ul>

    <div class="brand">
      <span class="brand-mark"></span>
      <div class="brand-name">Brightfen<br>Forgeworks</div>
    </div>

    <ul class="nav nav-right">
      <li>Axes</li>
      <li>Viking Jewelry</li>
      <li>Blog</li>
      <li>Shop</li>
    </ul>

    <h1 class="headline">Medieval swords, Battle Ready<br>Swords, Daggers and Armors</h1>

    <p class="intro">Brightfen Forgeworks’s battle ready Medieval swords, daggers and medieval weapons are<br>individually hand forged in Canada to look, feel and handle as the originals.</p>

    <a class="cta" href="#">LEARN MORE</a>

    <svg class="slider-dots" width="80" height="20" viewBox="0 0 80 20" aria-hidden="true">
      <circle cx="10" cy="10" r="8.5" fill="#ffffff"/>
      <circle cx="39" cy="10" r="8" fill="none" stroke="#e6e6e6" stroke-width="1.5"/>
      <circle cx="69" cy="10" r="8" fill="none" stroke="#e6e6e6" stroke-width="1.5"/>
    </svg>
  </main>
</body>
</html>
```